Business Card Project

We are a small consulting firm. You can experiment with any design.
Must have:
1) Company name - OLUNDEX International
2) Company slogan - simple solutions for complex problems
3) Name/Title/Phone/Email/WWW/ - use anything you like as an example.

Industry/Entity Type

Business

```html
<!DOCTYPE html>
<html lang="en">
<head>
<meta charset="utf-8">
<title>OLUNDEX International – Business Card</title>
<link rel="stylesheet" href="https://fonts.googleapis.com/css2?family=Jura:wght@400;500&display=swap">
<style>
  :root {
    --brand-blue: #0a7fd0;
    --brand-blue-light: #3aa0e6;
    --paper: #f3f3f1;
    --ink-grey: #5a5a5a;
    --white: #ffffff;
    --backdrop: #d9dadc;
  }
  * { box-sizing: border-box; margin: 0; padding: 0; }
  html, body { width: 1200px; height: 900px; overflow: hidden; }
  body {
    background: var(--backdrop);
    font-family: "Jura", "Segoe UI", sans-serif;
    position: relative;
  }
  .card {
    position: absolute;
    left: 290px;
    width: 620px;
    height: 350px;
    box-shadow: 0 6px 18px rgba(0,0,0,0.18);
    overflow: hidden;
  }

  /* Front */
  .card-front { top: 60px; background: var(--brand-blue); color: var(--white); }
  .brand {
    position: absolute; left: 70px; top: 100px;
    display: flex; align-items: center; gap: 30px;
  }
  .brand-dot {
    width: 92px; height: 92px; border-radius: 50%;
    background: var(--paper);
  }
  .brand-name { font-weight: 500; color: var(--white); line-height: 1; }
  .brand-name .main { display: block; font-size: 64px; letter-spacing: 2px; }
  .brand-name .sub { display: block; font-size: 22px; letter-spacing: 10px; margin-top: 6px; }
  .slogan {
    position: absolute; left: 70px; bottom: 40px;
    font-size: 21px; letter-spacing: 3px; color: var(--white);
  }

  /* Back */
  .card-back { top: 480px; background: var(--paper); }
  .person {
    position: absolute; left: 50px; top: 38px;
    display: flex; align-items: center; gap: 40px;
  }
  .person-dot { width: 84px; height: 84px; border-radius: 50%; background: var(--brand-blue); }
  .person-name { font-size: 27px; font-weight: 500; color: var(--ink-grey); letter-spacing: 0.5px; }
  .person-title { font-size: 17px; font-style: italic; color: var(--ink-grey); margin-top: 4px; }
  .contact-band {
    position: absolute; left: 0; right: 0; top: 175px; height: 125px;
    background: var(--brand-blue);
    display: grid; grid-template-columns: 1fr 1.2fr 1fr;
  }
  .contact-item {
    display: flex; flex-direction: column; align-items: center; justify-content: center;
    gap: 14px; color: var(--white); font-size: 19px; font-weight: 500;
  }
  .contact-item + .contact-item { border-left: 1px solid var(--brand-blue-light); }
  .contact-icon { width: 38px; height: 38px; }
</style>
</head>
<body>
  <section class="card card-front">
    <div class="brand">
      <div class="brand-dot"></div>
      <div class="brand-name">
        <span class="main">OLUNDEX</span>
        <span class="sub">INTERNATIONAL</span>
      </div>
    </div>
    <p class="slogan">simple solutions for complex problems</p>
  </section>

  <section class="card card-back">
    <div class="person">
      <div class="person-dot"></div>
      <div>
        <h1 class="person-name">DANIEL MOREAU</h1>
        <p class="person-title">Web Developer</p>
      </div>
    </div>
    <div class="contact-band">
      <div class="contact-item">
        <svg class="contact-icon" viewBox="0 0 38 38" fill="none" stroke="#fff" stroke-width="2">
          <circle cx="19" cy="19" r="17"/>
          <path d="M13 11c-1 1-2 3 0 7s5 7 9 9c2 1 3 0 4-1l-3-3-2 1c-2-1-4-3-5-5l1-2z" fill="#fff" stroke="none"/>
        </svg>
        <span>+41 79 555 18 46</span>
      </div>
      <div class="contact-item">
        <svg class="contact-icon" viewBox="0 0 38 38" fill="none" stroke="#fff" stroke-width="2">
          <circle cx="19" cy="19" r="17"/>
          <rect x="11" y="13" width="16" height="12"/>
          <path d="M11 13l8 7 8-7"/>
        </svg>
        <span>daniel@olundexint.com</span>
      </div>
      <div class="contact-item">
        <svg class="contact-icon" viewBox="0 0 38 38" fill="none" stroke="#fff" stroke-width="2">
          <circle cx="19" cy="19" r="17"/>
          <circle cx="19" cy="19" r="9" stroke-width="1.6"/>
          <ellipse cx="19" cy="19" rx="4" ry="9" stroke-width="1.4"/>
          <path d="M10 19h18M12 14h14M12 24h14" stroke-width="1.4"/>
        </svg>
        <span>www.olundexint.com</span>
      </div>
    </div>
  </section>
</body>
</html>
```